Flyer Design Project

We are looking to expand out business and provide Internet Service Provider (ISP) brokerage services. we need a clean elegant flyer that will be distributed in a hard copy (and possibly with a electronic format as well) describing out offerings. size should be A4 or smaller.
i attached a document with the logo QR and a general content.

design should be business like yet young and energetic. aesthetics and high end look is a must.

Target Market(s)

Small business owners

Industry/Entity Type

Electronic

```html
<!DOCTYPE html>
<html lang="en">
<head>
<meta charset="utf-8">
<title>Linkwise Solutions – Shop Your Internet and Phone Service</title>
<link rel="stylesheet" href="https://fonts.googleapis.com/css2?family=Jost:wght@400;600&family=Dosis:wght@400;500&display=swap">
<style>
  :root {
    --ink: #2b2b2b;
    --headline-ink: #1a1a1a;
    --accent-red: #a3262b;
    --panel-grey: #e6e6e6;
    --frame-grey: #b0b0b0;
    --hero-light: #f4f4f4;
    --hero-dark: #b4b4b4;
    --paper: #ffffff;
    --rule-red: #b86a6d;
  }
  * { margin: 0; padding: 0; box-sizing: border-box; }
  html, body { width: 928px; height: 1200px; overflow: hidden; background: var(--paper); }
  .flyer {
    position: relative;
    width: 928px; height: 1200px;
    border: 1px solid #555;
    font-family: "Jost", Arial, sans-serif;
    color: var(--ink);
    background: var(--paper);
  }
  .hero {
    position: absolute; left: 0; top: 0;
    width: 926px; height: 498px;
    background: radial-gradient(ellipse at 48% 40%, var(--hero-light) 0%, #dcdcdc 55%, var(--hero-dark) 100%);
  }
  .hero-illustration {
    position: absolute; left: 150px; top: 25px;
    width: 380px; height: 450px;
    border-radius: 40px;
    background: linear-gradient(135deg, #ececec 0%, #e4e4e4 45%, #c9a3a4 70%, #d9d9d9 100%);
    opacity: .85;
  }
  .headline {
    position: absolute; left: 432px; top: 200px;
    font-family: "Dosis", Arial, sans-serif;
    font-weight: 400;
    color: var(--headline-ink);
    text-transform: uppercase;
    line-height: 1;
  }
  .headline .line { display: block; white-space: nowrap; }
  .headline .line-1 { font-size: 38px; margin-left: 48px; letter-spacing: .5px; }
  .headline .line-2 { font-size: 38px; margin-top: 6px; }
  .headline .line-3 { font-size: 38px; margin-left: 72px; margin-top: 4px; }
  .headline .accent { color: var(--accent-red); font-size: 54px; font-weight: 500; }
  .content-frame {
    position: absolute; left: 29px; top: 498px;
    width: 870px; height: 672px;
    border: 3px solid var(--frame-grey); border-top: none;
  }
  .copy {
    position: absolute; left: 60px; width: 808px;
    font-size: 14.3px; line-height: 18px; text-align: justify;
  }
  .intro { top: 537px; }
  .history { top: 846px; }
  .approach { top: 936px; }
  .portfolio {
    position: absolute; left: 58px; width: 808px;
    background: var(--panel-grey);
    padding: 10px 12px 0 12px;
    font-size: 14px;
  }
  .portfolio-isp { top: 601px; height: 123px; }
  .portfolio-phone { top: 735px; height: 93px; }
  .portfolio h2 { font-size: 15px; font-weight: 600; margin-bottom: 14px; }
  .portfolio-list { list-style: none; }
  .portfolio-list li { display: flex; height: 18px; line-height: 18px; }
  .portfolio-isp .name { width: 125px; }
  .portfolio-phone .name { width: 133px; }
  .dash { width: 30px; }
  .more {
    position: absolute; right: 14px; bottom: 4px;
    color: var(--accent-red); font-size: 14px;
  }
  .rule {
    position: absolute; left: 60px; top: 1022px;
    width: 808px; height: 1px; background: var(--rule-red);
  }
  .brand-name {
    position: absolute; left: 96px; top: 1064px;
    font-size: 24px; font-weight: 600; color: var(--headline-ink);
  }
  .contact {
    position: absolute; left: 240px; top: 1028px;
    font-size: 17px; line-height: 22px; color: var(--ink);
  }
  .contact h3 { font-size: 19px; font-weight: 600; line-height: 24px; }
</style>
</head>
<body>
<div class="flyer">
  <header class="hero">
    <div class="hero-illustration" role="img" aria-label="3D illustration of a small white figure leaning against a large red telephone handset"></div>
    <h1 class="headline">
      <span class="line line-1">Shop your</span>
      <span class="line line-2"><span class="accent">Internet</span> and</span>
      <span class="line line-3"><span class="accent">Phone</span> service!</span>
    </h1>
  </header>

  <div class="content-frame"></div>

  <p class="copy intro">Linkwise Solutions Inc.offers tailor-made Internet and Phone service pricing services. Our unique access to a large number of carriers and providers enables us to find the best fit for your business specific needs and in turn will help your business maximize its resources.</p>

  <section class="portfolio portfolio-isp">
    <h2>Our ISP Solutions Portfolio Includes:</h2>
    <ul class="portfolio-list">
      <li><span class="name">Fiber Optics</span><span class="dash">-</span><span>EOC (Ethernet Over Copper)</span></li>
      <li><span class="name">DSL</span><span class="dash">-</span><span>Cable Modem</span></li>
      <li><span class="name">DS3</span><span class="dash">-</span><span>Fixed Wireless</span></li>
      <li><span class="name">T-1</span><span class="dash">-</span><span>Dedicated Private Site to Site Connections</span></li>
    </ul>
    <span class="more">And more....</span>
  </section>

  <section class="portfolio portfolio-phone">
    <h2>Our Telephone Solutions Portfolio Includes:</h2>
    <ul class="portfolio-list">
      <li><span class="name">SIP Trunking</span><span class="dash">-</span><span>Traditional Analog lines</span></li>
      <li><span class="name">PRI</span><span class="dash">-</span><span>Hosted PBX options</span></li>
    </ul>
    <span class="more">And more....</span>
  </section>

  <p class="copy history">Over the years we discovered that several of our clients were bound to the same services old communications providers and providers they had been using when they first established their business. They were never enhanced&amp;adjusted to fit todays IT needs and fast paced business environment. Our clients were losing productivity and were overpaying for existing outdated and inefficient services.</p>

  <p class="copy approach">While helping businesses increase efficiency by revitalizing their communication services, we had the opportunity to leverage the relationships and experiences we had with the various service providers and carriers and provide our clients the ability to choose the solution which will best fit their unique needs. We now offer these services on a larger scale enabling us to present businesses with multiple options at competitive rates.</p>

  <div class="rule"></div>

  <footer>
    <div class="brand-name">Linkwise</div>
    <div class="contact">
      <h3>Please contact us at</h3>
      <p>info@linkwisesolutions.net</p>
      <p>for inquiries about our offerings</p>
      <p>To learn more about our service offerings please visit our site at</p>
      <p>www.linkwisesolutions.net</p>
    </div>
  </footer>
</div>
</body>
</html>
```